Web Design Project

I am looking for a simple website to promote my business called Wyllard Benick Consulting. We provide consulting and implementation services for finance and supply chain processes and systems.

We want to project a professional but innovative image. I have attached a copy of our logo. It is not necessary to stick with the colours in the logo - we encourage you to experiment with the colours and even to change the colours of the logo to fit with your design. Although, on the front page we would like to have the logo with its original colours.

Required sections:
About
What we do
Clients
Contact
Updates

Target Market(s)

Medium to large companies including multi-nationals in all industries.

Industry/Entity Type

Finance

Requirements
Must have
• Required sections:
About
What we do
Clients
Contact

```html
<!DOCTYPE html>
<html lang="en">
<head>
<meta charset="utf-8">
<title>Wyllard Benick Consulting</title>
<link href="https://fonts.googleapis.com/css2?family=Arimo:wght@400;700&family=Montserrat:wght@700&family=Questrial&display=swap" rel="stylesheet">
<style>
  :root {
    --lime: #c2d62e;
    --navy: #04203d;
    --blue: #0a6cc9;
    --blue-deep: #0052a8;
    --link-blue: #1c86dc;
    --grey-text: #6b6b6b;
    --grey-head: #5a5a5a;
    --nav-grey: #555555;
    --rule: #cfcfcf;
    --footer: #000000;
    --white: #ffffff;
  }
  * { box-sizing: border-box; margin: 0; padding: 0; }
  html, body { width: 1105px; height: 1200px; overflow: hidden; }
  body { position: relative; background: var(--white); font-family: "Arimo", Arial, sans-serif; color: var(--grey-text); }

  .top-strip { position: absolute; left: 0; top: 0; width: 1105px; height: 5px; background: var(--lime); }
  .site-header { position: absolute; left: 0; top: 5px; width: 1105px; height: 113px;
    background: linear-gradient(#ffffff 0%, #ffffff 70%, #e6e6e6 100%); }
  .brand { position: absolute; left: 110px; top: 32px; display: flex; align-items: center; gap: 9px; }
  .brand-mark { width: 22px; height: 22px; border-radius: 50%; background: var(--lime); }
  .brand-name { font-family: "Questrial", sans-serif; font-size: 15px; line-height: 18px; color: var(--blue-deep); letter-spacing: .3px; }
  .main-nav { position: absolute; top: 55px; left: 0; width: 1105px; }
  .main-nav a { position: absolute; font-family: "Questrial", sans-serif; font-weight: 400; font-size: 15px; letter-spacing: .4px;
    color: var(--nav-grey); text-decoration: none; -webkit-text-stroke: .4px currentColor; }
  .main-nav a.active { color: var(--lime); }

  .hero { position: absolute; left: 0; top: 118px; width: 1105px; height: 406px;
    background: linear-gradient(100deg, #03203e 0%, #052a52 45%, #0a3f7a 62%, #0c5bb0 75%, #073469 90%, #021428 100%); }
  .hero-visual { position: absolute; left: 580px; top: 0; width: 525px; height: 406px;
    background: radial-gradient(circle at 60% 70%, #1566c2 0%, #0c4f9c 35%, rgba(6,40,80,0) 65%); }
  .hero-title { position: absolute; left: 115px; top: 124px; font-family: "Montserrat", sans-serif; font-weight: 700;
    font-size: 44px; line-height: 53px; letter-spacing: 1.5px; color: var(--lime); }
  .slider-dots { position: absolute; left: 124px; top: 382px; display: flex; gap: 25px; }
  .slider-dots span { width: 11px; height: 11px; border-radius: 50%; background: #bcc4cc; }
  .slider-dots span.current { background: #ffffff; }

  .feature { position: absolute; top: 551px; width: 276px; height: 155px; color: var(--white); text-align: center;
    background: radial-gradient(ellipse at 50% 10%, #1a86e4 0%, var(--blue) 45%, var(--blue-deep) 100%); }
  .feature::after { content: ""; position: absolute; left: 15px; right: 15px; bottom: -14px; height: 14px;
    background: radial-gradient(ellipse at 50% 0%, rgba(0,0,0,.22), rgba(0,0,0,0) 70%); }
  .feature svg { display: block; margin: 12px auto 0; }
  .feature h3 { font-family: "Questrial", sans-serif; font-weight: 400; font-size: 22px; letter-spacing: .5px; margin-top: 6px; }
  .feature p { font-size: 11px; line-height: 14px; margin: 10px 18px 0; }

  .section-title { position: absolute; top: 752px; font-family: "Questrial", sans-serif; font-size: 18px; color: var(--grey-head); letter-spacing: .3px; }
  .section-rule { position: absolute; top: 785px; height: 1px; background: var(--rule); }
  .thumb { position: absolute; left: 110px; top: 807px; width: 231px; height: 163px; border: 4px solid #dcdcdc;
    background: radial-gradient(circle at 50% 45%, #e9f3fc 0%, #9cc7ee 30%, #4a94d8 55%, #cfe2f4 100%); }
  .copy { position: absolute; top: 804px; text-align: justify; }
  .copy .lead { color: var(--link-blue); font-size: 12px; line-height: 16.5px; }
  .copy .lead small { font-size: 10.5px; }
  .copy .body { font-size: 10.5px; line-height: 16.6px; margin-top: 16px; color: var(--grey-text); }

  .client-strip { position: absolute; left: 110px; top: 1013px; width: 884px; height: 83px; border: 1px solid #d2d2d2;
    display: flex; align-items: center; justify-content: space-around; padding: 0 14px; }
  .client-name { font-family: "Arimo", sans-serif; font-weight: 700; font-size: 22px; color: #555555; }

  .site-footer { position: absolute; left: 0; top: 1122px; width: 1105px; height: 78px; background: var(--footer); }
  .copyright { position: absolute; left: 105px; top: 31px; font-size: 12px; color: #bdbdbd; }
  .social { position: absolute; right: 111px; top: 20px; display: flex; gap: 8px; }
  .social a { height: 30px; padding: 0 7px; background: #2b2b2b; color: #cfcfcf; font-size: 10px; line-height: 30px; text-decoration: none; }
</style>
</head>
<body>
  <div class="top-strip"></div>
  <header class="site-header">
    <div class="brand">
      <span class="brand-mark"></span>
      <span class="brand-name">Wyllard Benick<br>Consulting</span>
    </div>
    <nav class="main-nav">
      <a class="active" href="#about" style="left:568px">ABOUT</a>
      <a href="#what-we-do" style="left:665px">WHAT WE DO</a>
      <a href="#clients" style="left:807px">CLIENTS</a>
      <a href="#contact" style="left:911px">CONTACT</a>
    </nav>
  </header>

  <section class="hero" id="about">
    <div class="hero-visual" role="img" aria-label="Blue globe photograph on a dark background"></div>
    <h1 class="hero-title">CONSULTING<br>&amp; IMPLEMENTATION<br>SERVICES</h1>
    <div class="slider-dots"><span class="current"></span><span></span><span></span></div>
  </section>

  <article class="feature" style="left:110px">
    <svg width="40" height="40" viewBox="0 0 40 40" aria-hidden="true">
      <path d="M8 34 C8 18 18 6 36 4 C34 22 24 32 8 34 Z" fill="#fff"/>
      <path d="M6 36 L30 10" stroke="#0a6cc9" stroke-width="2"/>
    </svg>
    <h3>OUR VISION</h3>
    <p>Sed ut perspiciatis unde omnis iste natus error sit voluptatem accusantium doloremque laudantium, totam rem aperiam, eaque ipsa</p>
  </article>
  <article class="feature" style="left:413px">
    <svg width="40" height="40" viewBox="0 0 40 40" aria-hidden="true">
      <path d="M11 4 H29 V14 C29 20 25 24 20 24 C15 24 11 20 11 14 Z" fill="#fff"/>
      <path d="M11 8 H5 C5 15 8 18 12 18 M29 8 H35 C35 15 32 18 28 18" stroke="#fff" stroke-width="2.5" fill="none"/>
      <rect x="18" y="24" width="4" height="7" fill="#fff"/>
      <rect x="12" y="31" width="16" height="5" fill="#fff"/>
    </svg>
    <h3>OUR GOAL</h3>
    <p>Sed ut perspiciatis unde omnis iste natus error sit voluptatem accusantium doloremque laudantium, totam rem aperiam, eaque ipsa</p>
  </article>
  <article class="feature" style="left:717px">
    <svg width="40" height="40" viewBox="0 0 40 40" aria-hidden="true">
      <path d="M20 2 C29 2 34 9 34 15 C34 22 27 25 26 31 H14 C13 25 6 22 6 15 C6 9 11 2 20 2 Z" fill="#fff"/>
      <rect x="14" y="32" width="12" height="3" fill="#fff"/>
      <rect x="16" y="36" width="8" height="3" fill="#fff"/>
    </svg>
    <h3>SOLUTION</h3>
    <p>Sed ut perspiciatis unde omnis iste natus error sit voluptatem accusantium doloremque laudantium, totam rem aperiam, eaque ipsa</p>
  </article>

  <h2 class="section-title" id="what-we-do" style="left:110px">WHAT WE DO</h2>
  <div class="section-rule" style="left:110px;width:580px"></div>
  <h2 class="section-title" style="left:717px">HOW IT WORKS</h2>
  <div class="section-rule" style="left:717px;width:277px"></div>

  <div class="thumb" role="img" aria-label="Glass globe resting on financial papers, in light blue tones"></div>
  <div class="copy" style="left:355px;width:335px">
    <p class="lead">Sed ut perspiciatis unde omnis iste natus error sit voluptatem accusantium doloremque laudantium,</p>
    <p class="body">totam rem aperiam, eaque ipsa quae ab illo inventore veritatis et quasi architecto beatae vitae dicta sunt explicabo. Nemo enim ipsam voluptatem quia voluptas sit aspernatur aut odit aut fugit, sed quia consequuntur magni dolores eos qui ratione voluptatem sequi nesciunt. Neque porro quisquam est, qui dolorem ipsum quia dolor sit amet, consectetur, adipisci velit, sed quia non numquam eius modi tempora incidunt ut labore et dolore magnam aliquam quaerat volup-</p>
  </div>
  <div class="copy" style="left:717px;width:277px">
    <p class="lead">Sed ut perspiciatis unde omnis iste natus error sit voluptatem accusam doloremque laudantium,<small>tam rem aperiam, eaque ipsa quae ab illo inventore</small></p>
    <p class="body">veritatis et quasi architecto beatae vitae dicta sunt expli-cabo. Nemo enim ipsam voluptatem quia voluptas sit aspernatur aut odit aut fugit, sed quia consequuntur magni dolores eos qui ratione voluptatem sequi nesciunt. Neque porro quisquam est, qui dolorem ipsum quia dolor sit amet, consectetur, adipisci velit, sed quia non</p>
  </div>

  <section class="client-strip" id="clients" aria-label="Clients">
    <span class="client-name">Norvale</span>
    <span class="client-name">Tradelot</span>
    <span class="client-name">Arcforge</span>
    <span class="client-name">Searchly</span>
    <span class="client-name">Kaimoto</span>
    <span class="client-name">Lumeo</span>
  </section>

  <footer class="site-footer" id="contact">
    <p class="copyright">© 2013 Wyllard Benick Consulting.. | All rights reserved.</p>
    <div class="social">
      <a href="#">Kinnect</a>
      <a href="#">Murmur</a>
      <a href="#">Reelo</a>
      <a href="#">Orbita</a>
    </div>
  </footer>
</body>
</html>
```